Crowdsourced Research Platform: VELTA Polls

VELTA Polls is an acronym for Varied Estimates Linking Topical Attitudes (VELTA) Polls. This is a research effort to format and combine multiple sources of public opinion data from around the world into merged datasets. The website will at first mainly act as a quality control hub and distribution point for official dataset releases. It will provide resources such as codebooks, development guidelines, and instructional videos for crowdsourcing continued expansion of the resource. We need a coded (HTML and CSS) website design and associated files to launch the website with ease. We purchased the domain www.veltapolls.org, but access is blocked while it is under construction.

The website design should be based on a logo recently commissioned (see attached). The design should be simple and professional with lots of white space. We would like the logo on the top left of all pages and the primary navigation menu along the top-right of all pages. The primary navigation menu should have a simple mouse-over effect and the main menu items should expand with secondary drop-down options. The footer should include a few columns with headings and links to different pages. The website layout should be dynamic and expand its width to fit different sized screens. There will be a lot of data and information displayed in tables, so we would like the CSS coding and website design to include tables designed to match the website theme. The main graphical content will be data visualisations such as pie/bar charts, histograms, scatter plots, heat maps, moving average trend lines etc. We would therefore like the design to include modular sections (boxes matching theme to display plots/graphs/etc) that can visually display these types of figures with text/caption underneath to explain the data visualizations.

For more information and written placeholder content, designers should read the attached documents to get a better idea about the project. Some draft working papers using merged datsets have been included for reference and you can use these for their examples of data visualizations and use the written content for filling in page content.

Target Market(s)

The primary target audience will be academics in universities and research institutes. The resource will be most useful to quantitative social scientists, particularly political scientists and sociologists, but any discipline concerned with us humans could find the resource useful. Others such as graduate-level university students, civil servants in government departments, members of research institutions, and policy researchers in non-profit organizations will also find the resource useful.

Coding

Coded - Design and coding required

Number of Pages Required

3 page

Font styles to use
Sans Serif

Colors

Designer to choose colors to be used in the design.

Requirements
Must have
• HTML and CSS coding (not Wordpress)
Nice to have
• Content boxes to display data visualizations alongside articles.

```html
<!DOCTYPE html>
<html lang="en">
<head>
<meta charset="utf-8">
<title>VELTA Polls</title>
<link href="https://fonts.googleapis.com/css2?family=Montserrat:wght@400;500;600;700&display=swap" rel="stylesheet">
<style>
:root{
  --blue:#1a6fbf;
  --blue-dark:#165a9c;
  --blue-deep:#124c86;
  --ink:#1f2a36;
  --text:#555c63;
  --muted:#8a9097;
  --grey-bg:#f0f0f0;
  --line:#e1e1e1;
  --white:#ffffff;
  --btn-dark:#3e4145;
}
*{box-sizing:border-box;margin:0;padding:0}
html,body{width:1200px;height:4905px;overflow:hidden}
body{font-family:"Montserrat",Arial,sans-serif;color:var(--text);background:var(--white);position:relative}
section,header,footer{position:absolute;left:0;width:1200px}
.section-title{position:absolute;left:0;width:1200px;text-align:center;font-size:30px;font-weight:600;color:var(--ink);letter-spacing:.5px}
.section-title span{color:var(--blue)}
.section-title::after{content:"";display:block;width:70px;height:3px;background:var(--blue);margin:16px auto 0}
p{font-size:13.5px;line-height:1.6}

/* header */
.site-header{top:0;height:92px;background:var(--white);border-bottom:1px solid var(--line)}
.brand{position:absolute;left:100px;top:28px;display:flex;align-items:center;gap:12px;font-size:26px;font-weight:600;color:var(--blue)}
.brand-dot{width:30px;height:30px;border-radius:50%;background:var(--blue)}
.main-nav{position:absolute;right:100px;top:36px;display:flex;gap:38px;font-size:15px;font-weight:600;color:var(--ink)}
.main-nav .active{color:var(--blue)}

/* hero */
.hero{top:92px;height:516px}
.hero-photo{position:absolute;inset:0;background:linear-gradient(90deg,#9aa3ab 0%,#c9ced2 40%,#aeb8c0 70%,#7f8d98 100%)}
.hero-title{position:absolute;right:100px;top:50px;font-size:56px;font-weight:700;color:var(--white)}
.hero-text{position:absolute;right:100px;top:135px;width:420px;text-align:right;color:var(--white);font-size:14px}
.btn-outline{position:absolute;right:100px;top:232px;width:128px;height:54px;border:2px solid var(--white);color:var(--white);font-size:15px;display:flex;align-items:center;justify-content:center}
.slider-dots{position:absolute;left:100px;bottom:120px;display:flex;gap:9px}
.slider-dots i{width:12px;height:12px;border-radius:50%;background:rgba(255,255,255,.6)}
.slider-dots i:first-child{background:var(--white)}

/* about */
.about{top:608px;height:520px;background:var(--white)}
.about h2{position:absolute;left:100px;top:88px;font-size:30px;font-weight:600;color:var(--ink)}
.about h2 span{color:var(--blue)}
.about h2::after{content:"";display:block;width:70px;height:3px;background:var(--blue);margin-top:16px}
.about-copy{position:absolute;left:100px;top:172px;width:520px}
.about-copy p{margin-bottom:16px}
.btn-blue{display:inline-flex;align-items:center;justify-content:center;background:var(--blue);color:var(--white);font-size:15px;font-weight:500}
.about .btn-blue{position:absolute;left:100px;top:372px;width:128px;height:54px}
.about-photo{position:absolute;left:640px;top:0;width:560px;height:520px;background:linear-gradient(135deg,#ffffff 0%,#f1efec 45%,#e2d7cf 75%,#c9b3a5 100%)}

/* used by */
.used-by{top:1128px;height:566px;background:var(--grey-bg)}
.used-by .section-title{top:64px}
.audience-card{position:absolute;top:167px;width:312px;height:296px;background:var(--white);border:1px solid #ddd;box-shadow:0 14px 14px -10px rgba(0,0,0,.22);text-align:center;padding:0 20px}
.audience-icon{width:112px;height:112px;border-radius:50%;background:var(--blue);margin:25px auto 40px;display:flex;align-items:center;justify-content:center}
.audience-card h3{font-size:17px;font-weight:700;color:var(--blue-deep);margin-bottom:10px}
.audience-card p{font-size:13px;line-height:1.45}

/* resources */
.resources{top:1694px;height:621px;background:var(--white)}
.resources .section-title{top:80px}
.resource-card{position:absolute;top:193px;width:313px;height:206px;display:flex;align-items:center;justify-content:center;text-align:center;color:var(--white);font-size:24px;font-weight:600;line-height:1.5;text-transform:uppercase}
.resource-card.tone-a{background:linear-gradient(135deg,#6d6a66,#a8a39c)}
.resource-card.tone-b{background:linear-gradient(135deg,#1d5e9d,#3f86c6)}
.resource-card.tone-c{background:linear-gradient(135deg,#7c7d80,#b7b9bb)}
.resource-btn{position:absolute;top:484px;width:190px;height:44px;font-size:14px;font-weight:500;color:var(--white);display:flex;align-items:center;justify-content:center}
.resource-btn.dark{background:var(--btn-dark)}
.resource-btn.blue{background:var(--blue)}

/* surveys */
.survey-block{background:var(--white)}
.survey-block.grey{background:var(--grey-bg)}
.our-surveys-head{top:2315px;height:140px;background:var(--grey-bg)}
.our-surveys-head .section-title{top:70px}
.chart-card{position:absolute;width:375px;background:var(--white);border:1px solid #ddd;box-shadow:0 6px 12px rgba(0,0,0,.12)}
.survey-copy{position:absolute;width:505px}
.survey-copy h3{font-size:22px;font-weight:700;color:var(--blue-deep);margin-bottom:18px}
.survey-copy p{font-size:13.5px;margin-bottom:14px;color:var(--text)}

/* variables */
.variables{top:3957px;height:572px;background:var(--grey-bg)}
.variables .section-title{top:70px}
.var-grid{position:absolute;left:100px;top:168px;width:1000px;height:335px;display:grid;grid-template-columns:repeat(3,1fr);grid-template-rows:repeat(2,1fr)}
.var-cell{padding:28px 30px 0 30px;display:flex;gap:18px}
.var-cell.light{background:var(--white)}
.var-cell.light h4{color:var(--blue-deep)}
.var-cell.light p{color:var(--muted)}
.var-cell.dark{background:var(--blue)}
.var-cell.dark h4,.var-cell.dark p{color:var(--white)}
.var-cell h4{font-size:19px;font-weight:700;margin-bottom:10px}
.var-cell p{font-size:12.5px;line-height:1.5}
.var-icon{flex:0 0 38px;height:38px}

/* footer */
.site-footer{top:4529px;height:376px;background:var(--blue)}
.footer-brand{position:absolute;top:72px;left:0;width:1200px;display:flex;justify-content:center;align-items:center;gap:14px;font-size:36px;font-weight:600;color:var(--white)}
.footer-brand .brand-dot{width:42px;height:42px;background:var(--white)}
.footer-contact{position:absolute;top:178px;left:0;width:1200px;display:flex;justify-content:center;gap:60px;color:var(--white);font-size:15px;font-weight:600}
.footer-contact span{display:flex;align-items:center;gap:12px}
.footer-rule{position:absolute;left:100px;width:1000px;height:1px;background:rgba(255,255,255,.4)}
.footer-nav{position:absolute;top:246px;left:0;width:1200px;display:flex;justify-content:center;gap:36px;color:var(--white);font-size:13px;font-weight:600}
.footer-bottom{position:absolute;left:0;bottom:0;width:1200px;height:62px;background:var(--blue-dark);display:flex;align-items:center;justify-content:center;color:var(--white);font-size:13px;font-weight:600}
</style>
</head>
<body>

<header class="site-header">
  <div class="brand"><span class="brand-dot"></span>VELTA Polls</div>
  <nav class="main-nav">
    <span class="active">HOME</span><span>ABOUT</span><span>HELP</span><span>SOURCES</span><span>VARIABLES</span><span>CONTACT</span>
  </nav>
</header>

<section class="hero">
  <div class="hero-photo" role="img" aria-label="Smiling man holding a tablet beside satisfaction faces and tick boxes"></div>
  <h1 class="hero-title">VELTA Polls</h1>
  <p class="hero-text">VELTA Polls make it easier to work with multiple sources of public opinion data. It does so by formatting variables.</p>
  <span class="btn-outline">Read More</span>
  <div class="slider-dots"><i></i><i></i><i></i><i></i></div>
</section>

<section class="about">
  <h2>ABOUT <span>VELTA POLLS</span></h2>
  <div class="about-copy">
    <p>VELTA Polls make it easier to work with multiple sources of public opinion data. It does so by format ting variables for consistency and merging datasets together. The current merged dataset includes millions of respondents, covers most countries in the world, and extends back decades. This increased variation over time and space enables answering.</p>
    <p>The ultimate goal is to format every variable from every round of every publicly available survey source that takes nationally representative samples of adults.</p>
  </div>
  <span class="btn-blue">Read More</span>
  <div class="about-photo" role="img" aria-label="Hand ticking a survey checkbox with a red pencil"></div>
</section>

<section class="used-by">
  <h2 class="section-title">SURVEYS <span>USED BY</span></h2>
  <div class="audience-card" style="left:100px">
    <div class="audience-icon"><svg width="50" height="50" viewBox="0 0 50 50" fill="none" stroke="#fff" stroke-width="4"><circle cx="21" cy="21" r="13"/><line x1="31" y1="31" x2="44" y2="44" stroke-linecap="round"/></svg></div>
    <h3>RESEARCHERS</h3>
    <p>VELTA Polls make it easier to work with multiple sources of public opinion data. It does.</p>
  </div>
  <div class="audience-card" style="left:444px">
    <div class="audience-icon"><svg width="54" height="54" viewBox="0 0 54 54" fill="#fff"><polygon points="27,6 50,16 27,26 4,16"/><circle cx="27" cy="32" r="8"/><path d="M12 52c0-10 7-14 15-14s15 4 15 14z"/></svg></div>
    <h3>STUDENTS</h3>
    <p>VELTA Polls make it easier to work with multiple sources of public opinion data. It does.</p>
  </div>
  <div class="audience-card" style="left:788px">
    <div class="audience-icon"><svg width="54" height="54" viewBox="0 0 54 54" fill="#fff"><rect x="6" y="6" width="42" height="44"/><g fill="#1a6fbf"><rect x="12" y="12" width="6" height="6"/><rect x="24" y="12" width="6" height="6"/><rect x="36" y="12" width="6" height="6"/><rect x="12" y="24" width="6" height="6"/><rect x="24" y="24" width="6" height="6"/><rect x="36" y="24" width="6" height="6"/><rect x="22" y="38" width="10" height="12"/></g></svg></div>
    <h3>GOVERNMENT AGENCIES</h3>
    <p>VELTA Polls make it easier to work with multiple sources of public opinion data. It does.</p>
  </div>
</section>

<section class="resources">
  <h2 class="section-title">OUR <span>RESOURCES</span></h2>
  <div class="resource-card tone-a" style="left:100px" role="img" aria-label="Open codebook pages">Codebooks</div>
  <div class="resource-card tone-b" style="left:443px" role="img" aria-label="Team reviewing development guidelines">Development<br>Guidelines</div>
  <div class="resource-card tone-c" style="left:787px" role="img" aria-label="People watching an instructional video">Instructional<br>Videos</div>
  <span class="resource-btn dark" style="left:161px">Download Codebooks</span>
  <span class="resource-btn blue" style="left:504px">Download Guidelines</span>
  <span class="resource-btn dark" style="left:848px">Download Videos</span>
</section>

<section class="our-surveys-head"><h2 class="section-title">OUR SURVEYS</h2></section>

<section class="survey-block grey" style="top:2455px;height:360px">
  <div class="chart-card" style="left:100px;top:55px;height:175px">
    <svg width="375" height="175" viewBox="0 0 375 175">
      <g fill="#c9cdd2"><circle cx="60" cy="22" r="4"/><circle cx="90" cy="22" r="4"/><circle cx="120" cy="22" r="4"/><circle cx="150" cy="22" r="4"/><circle cx="180" cy="22" r="4"/><circle cx="210" cy="22" r="4"/></g>
      <circle cx="245" cy="22" r="8" fill="#4a9fd8"/><circle cx="275" cy="22" r="7" fill="#1a6fbf"/><circle cx="305" cy="22" r="7" fill="#124c86"/><circle cx="330" cy="22" r="6" fill="#d9534f"/>
      <rect x="20" y="40" width="330" height="118" fill="#f3f5f7"/>
      <rect x="20" y="48" width="300" height="14" rx="7" fill="#8fc4e8"/>
      <rect x="20" y="68" width="250" height="14" rx="7" fill="#4a9fd8"/>
      <rect x="20" y="88" width="320" height="14" rx="7" fill="#1a6fbf"/>
      <rect x="20" y="108" width="200" height="14" rx="7" fill="#2c5f8f"/>
      <rect x="20" y="128" width="275" height="14" rx="7" fill="#7fa8c9"/>
    </svg>
  </div>
  <div class="survey-copy" style="left:530px;top:70px">
    <h3>NEMO ENIM IPSAM</h3>
    <p>Nemo enim ipsam voluptatem quia voluptas sit aspernatur aut odit aut fugit, sed quia consequuntur magni dolores eos qui ratione voluptatem sequi nesciunt. Neque porro quisquam est, qui dolorem ipsum quia dolor sit amet, consectetur, adipisci velit, sed quia non numquam</p>
    <p>Sed ut perspiciatis unde omnis iste natus error sit voluptatem accusantium dolorem que laudantium, totam rem aperiam, eaque ipsa quae ab illo inventore veritatis et quasi architecto beatae vitae dicta sunt explicabo.</p>
  </div>
</section>

<section class="survey-block" style="top:2815px;height:345px">
  <div class="survey-copy" style="left:100px;top:70px">
    <h3>VOLUPTATEM QUIA VOLUPTAS</h3>
    <p>Nemo enim ipsam voluptatem quia voluptas sit aspernatur aut odit aut fugit, sed quia consequuntur magni dolores eos qui ratione voluptatem sequi nesciunt. Neque porro quisquam est, qui dolorem ipsum quia dolor sit amet, consectetur, adipisci velit, sed quia non numquam</p>
    <p>Sed ut perspiciatis unde omnis iste natus error sit voluptatem accusantium dolorem que laudantium, totam rem aperiam, eaque ipsa quae ab illo inventore veritatis et quasi architecto beatae vitae dicta sunt explicabo.</p>
  </div>
  <div class="chart-card" style="left:725px;top:65px;height:250px">
    <svg width="375" height="250" viewBox="0 0 375 250">
      <line x1="40" y1="130" x2="340" y2="130" stroke="#ccc"/>
      <g fill="#f0b323"><rect x="50" y="90" width="12" height="40"/><rect x="85" y="75" width="12" height="55"/><rect x="120" y="60" width="12" height="70"/><rect x="155" y="70" width="12" height="60"/><rect x="190" y="50" width="12" height="80"/><rect x="225" y="45" width="12" height="85"/><rect x="260" y="38" width="12" height="92"/><rect x="295" y="30" width="12" height="100"/></g>
      <g fill="#1a6fbf"><rect x="64" y="100" width="12" height="30"/><rect x="99" y="95" width="12" height="35"/><rect x="134" y="85" width="12" height="45"/><rect x="169" y="88" width="12" height="42"/><rect x="204" y="78" width="12" height="52"/><rect x="239" y="70" width="12" height="60"/><rect x="274" y="62" width="12" height="68"/><rect x="309" y="55" width="12" height="75"/></g>
      <g transform="translate(0,150)">
        <circle cx="70" cy="35" r="24" fill="#1a6fbf"/><path d="M70 35 L70 11 A24 24 0 0 1 92 44 Z" fill="#f0b323"/>
        <circle cx="150" cy="35" r="24" fill="#1a6fbf"/><path d="M150 35 L150 11 A24 24 0 1 1 130 48 Z" fill="#f0b323"/>
        <circle cx="230" cy="35" r="24" fill="#1a6fbf"/><path d="M230 35 L230 11 A24 24 0 0 1 248 52 Z" fill="#f0b323"/>
        <circle cx="310" cy="35" r="24" fill="#1a6fbf"/><path d="M310 35 L310 11 A24 24 0 1 1 288 26 Z" fill="#f0b323"/>
        <g fill="#d5d8dc"><rect x="45" y="70" width="50" height="5"/><rect x="125" y="70" width="50" height="5"/><rect x="205" y="70" width="50" height="5"/><rect x="285" y="70" width="50" height="5"/></g>
      </g>
    </svg>
  </div>
</section>

<section class="survey-block grey" style="top:3160px;height:360px">
  <div class="chart-card" style="left:100px;top:90px;height:250px">
    <svg width="375" height="250" viewBox="0 0 375 250">
      <rect x="20" y="20" width="80" height="6" fill="#c9cdd2"/><rect x="180" y="20" width="150" height="4" fill="#e0e0e0"/>
      <g stroke="#eee"><line x1="30" y1="60" x2="270" y2="60"/><line x1="30" y1="100" x2="270" y2="100"/><line x1="30" y1="140" x2="270" y2="140"/><line x1="30" y1="180" x2="270" y2="180"/></g>
      <path d="M30 70 L80 60 L130 85 L180 55 L230 75 L270 62 L270 200 L30 200 Z" fill="#1a6fbf" opacity=".8"/>
      <path d="M30 110 L80 95 L130 120 L180 100 L230 115 L270 105 L270 200 L30 200 Z" fill="#6a4fa3" opacity=".7"/>
      <path d="M30 150 L80 140 L130 160 L180 145 L230 150 L270 140 L270 200 L30 200 Z" fill="#2bb3a3" opacity=".8"/>
      <g><rect x="290" y="80" width="10" height="10" fill="#1a6fbf"/><rect x="305" y="83" width="45" height="4" fill="#ccc"/><rect x="290" y="105" width="10" height="10" fill="#6a4fa3"/><rect x="305" y="108" width="45" height="4" fill="#ccc"/><rect x="290" y="130" width="10" height="10" fill="#2bb3a3"/><rect x="305" y="133" width="45" height="4" fill="#ccc"/></g>
    </svg>
  </div>
  <div class="survey-copy" style="left:530px;top:75px">
    <h3>SED UT PERSPICIATIS</h3>
    <p>Nemo enim ipsam voluptatem quia voluptas sit aspernatur aut odit aut fugit, sed quia consequuntur magni dolores eos qui ratione voluptatem sequi nesciunt. Neque porro quisquam est, qui dolorem ipsum quia dolor sit amet, consectetur, adipisci velit, sed quia non numquam</p>
    <p>Sed ut perspiciatis unde omnis iste natus error sit voluptatem accusantium dolorem que laudantium, totam rem aperiam, eaque ipsa quae ab illo inventore veritatis et quasi architecto beatae vitae dicta sunt explicabo.</p>
  </div>
</section>

<section class="survey-block" style="top:3520px;height:437px">
  <div class="survey-copy" style="left:100px;top:85px">
    <h3>UNDE OMNIS NATUS</h3>
    <p>Nemo enim ipsam voluptatem quia voluptas sit aspernatur aut odit aut fugit, sed quia consequuntur magni dolores eos qui ratione voluptatem sequi nesciunt. Neque porro quisquam est, qui dolorem ipsum quia dolor sit amet, consectetur, adipisci velit, sed quia non numquam</p>
    <p>Sed ut perspiciatis unde omnis iste natus error sit voluptatem accusantium dolorem que laudantium, totam rem aperiam, eaque ipsa quae ab illo inventore veritatis et quasi architecto beatae vitae dicta sunt explicabo.</p>
  </div>
  <div class="chart-card" style="left:725px;top:75px;height:300px">
    <svg width="375" height="300" viewBox="0 0 375 300">
      <rect x="25" y="25" width="150" height="7" fill="#3a3f45"/>
      <line x1="40" y1="200" x2="340" y2="200" stroke="#ccc"/>
      <polyline points="50,170 90,150 130,160 170,120 210,135 250,110 290,125 330,95" fill="none" stroke="#1a6fbf" stroke-width="3"/>
      <polyline points="50,185 90,175 130,180 170,165 210,170 250,150 290,160 330,140" fill="none" stroke="#f0b323" stroke-width="3"/>
      <g fill="#fff" stroke="#1a6fbf" stroke-width="2"><circle cx="50" cy="170" r="5"/><circle cx="90" cy="150" r="5"/><circle cx="130" cy="160" r="5"/><circle cx="170" cy="120" r="5"/><circle cx="210" cy="135" r="5"/><circle cx="250" cy="110" r="5"/><circle cx="290" cy="125" r="5"/><circle cx="330" cy="95" r="5"/></g>
      <g fill="#d9534f"><circle cx="50" cy="185" r="4"/><circle cx="130" cy="180" r="4"/><circle cx="210" cy="170" r="4"/><circle cx="290" cy="160" r="4"/></g>
      <g><rect x="40" y="225" width="30" height="22" fill="#e9534f"/><rect x="80" y="225" width="30" height="22" fill="#f0b323"/><rect x="120" y="225" width="30" height="22" fill="#2bb3a3"/><rect x="160" y="225" width="30" height="22" fill="#1a6fbf"/><rect x="200" y="225" width="30" height="22" fill="#6a4fa3"/><rect x="240" y="225" width="30" height="22" fill="#e9534f"/><rect x="280" y="225" width="30" height="22" fill="#2bb3a3"/></g>
    </svg>
  </div>
</section>

<section class="variables">
  <h2 class="section-title">OUR <span>VARIABLES</span></h2>
  <div class="var-grid">
    <div class="var-cell light">
      <svg class="var-icon" viewBox="0 0 38 38" fill="#1a6fbf"><polygon points="19,2 36,19 19,36 2,19"/><circle cx="19" cy="19" r="6" fill="#fff"/></svg>
      <div><h4>Social Trust</h4><p>At the respondent level, the common variable distinguishes between trusting and less trusting people.</p></div>
    </div>
    <div class="var-cell dark">
      <svg class="var-icon" viewBox="0 0 38 38" fill="#fff"><path d="M19 34 L4 19 A8 8 0 0 1 19 8 A8 8 0 0 1 34 19 Z"/></svg>
      <div><h4>Satisfaction</h4><p>At the respondent level, the common variable indicates whether respondents are satisfied.</p></div>
    </div>
    <div class="var-cell light">
      <svg class="var-icon" viewBox="0 0 38 38"><polygon points="2,36 36,36 36,2" fill="#1a6fbf"/></svg>
      <div><h4>Age</h4><p>This respondent-level variable repre sents age using three categories: under 30, 30 to 50, over 50.</p></div>
    </div>
    <div class="var-cell dark">
      <svg class="var-icon" viewBox="0 0 38 38" fill="none" stroke="#fff" stroke-width="3"><circle cx="14" cy="22" r="9"/><circle cx="24" cy="14" r="9"/></svg>
      <div><h4>Gender</h4><p>This respondent-level variable indica tes whether respondents are male or female.</p></div>
    </div>
    <div class="var-cell light">
      <svg class="var-icon" viewBox="0 0 38 38" fill="#1a6fbf"><polygon points="19,6 36,14 19,22 2,14"/><path d="M9 18 v9 c0 4 20 4 20 0 v-9 l-10 5z"/></svg>
      <div><h4>Education</h4><p>This respondent-level variable cate gorises respondents within three educational levels.</p></div>
    </div>
    <div class="var-cell dark">
      <svg class="var-icon" viewBox="0 0 38 38"><circle cx="19" cy="19" r="16" fill="#fff"/><text x="19" y="26" text-anchor="middle" font-family="Montserrat,sans-serif" font-size="19" font-weight="700" fill="#1a6fbf">$</text></svg>
      <div><h4>Income</h4><p>This respondent-level variable cate gorises respondents into three income groups.</p></div>
    </div>
  </div>
</section>

<footer class="site-footer">
  <div class="footer-brand"><span class="brand-dot"></span>VELTA Polls</div>
  <div class="footer-contact">
    <span><svg width="28" height="28" viewBox="0 0 28 28" fill="none" stroke="#fff" stroke-width="2"><circle cx="14" cy="14" r="12"/><path d="M10 8 l3 3 -2 2 c1 2 2 3 4 4 l2 -2 3 3 -2 2 c-5 0 -10 -5 -10 -10z" fill="#fff" stroke="none"/></svg>PHONE: 1 - 800 - 555 - 0142</span>
    <span><svg width="28" height="28" viewBox="0 0 28 28" fill="none" stroke="#fff" stroke-width="2"><circle cx="14" cy="14" r="12"/><rect x="8" y="10" width="12" height="9"/><polyline points="8,10 14,15 20,10"/></svg>EMAIL: info@veltapolls.org</span>
  </div>
  <div class="footer-rule" style="top:228px"></div>
  <nav class="footer-nav"><span>HOME</span><span>|</span><span>ABOUT</span><span>|</span><span>HELP</span><span>|</span><span>SOURCES</span><span>|</span><span>VARIABLES</span><span>|</span><span>CONTACT US</span></nav>
  <div class="footer-rule" style="top:286px"></div>
  <div class="footer-bottom">Copyright © 2018 VELTA Polls. All Rights Reserved.</div>
</footer>

</body>
</html>
```